Professional Modern Website Design

We are a premium IT services provider to the financial industry based in London. Our company is called Veltra our current holding page is www.veltra-example.co.uk. We require a new website to match our new corporate identity. This project is for the design phase only. Development will be handled in-house. I have attached examples of wire frames we have developed (although open to suggestions for improvement) Our brand document that should demonstrate current brand, inc how we communicate to potential clients and finally mostly completed web-content.
We are looking for designers that can create something that sets us apart from our competitors.
Target Market(s)
IT Decision makers in Finance companies such as; hedge funds, private investment banks etc
Industry/Entity Type
Financial
Number of Pages Required
5+ page
Requirements
Must have
- hexagon elements in the design, unique design.
Nice to have
- Blog and social media feeds
Should not have
- Should not resemble a downloaded template

```html
<!DOCTYPE html>
<html lang="en">
<head>
<meta charset="utf-8">
<title>Veltra — IT Integration for Finance</title>
<link href="https://fonts.googleapis.com/css2?family=Raleway:wght@300;400;500;600;700&family=Open+Sans:wght@400;600&display=swap" rel="stylesheet">
<style>
:root{
  --orange:#f29111;
  --amber:#f9b21b;
  --ink:#333a44;
  --muted:#7b8088;
  --night:#1b222c;
  --night-2:#2b3440;
  --paper:#ffffff;
  --mist:#f3f4f5;
  --line:#dadde1;
}
*{box-sizing:border-box;margin:0;padding:0}
html,body{width:1200px;height:3352px;overflow:hidden}
body{font-family:"Raleway",sans-serif;color:var(--ink);background:var(--paper);position:relative}
section,header,footer,nav{position:absolute;left:0;width:1200px}
.center{text-align:center}
.section-title{font-weight:300;font-size:38px;color:var(--ink);text-align:center}
.section-lead{font-family:"Open Sans",sans-serif;font-size:15px;line-height:1.75;color:var(--muted);text-align:center;margin:0 auto}

/* hero */
.hero{top:0;height:788px;background:linear-gradient(180deg,#2a313c 0%,#1d242e 55%,#151a22 100%)}
.hero-backdrop{position:absolute;inset:0;background:linear-gradient(120deg,rgba(70,80,95,.55) 0%,rgba(30,36,46,.2) 40%,rgba(60,70,84,.5) 70%,rgba(20,25,32,.3) 100%)}
.brand-mark{position:absolute;display:flex;align-items:center;gap:10px;font-weight:700;color:var(--orange)}
.brand-mark .dot{width:14px;height:14px;background:var(--orange)}
.hero .brand-mark{top:165px;left:0;width:1200px;justify-content:center;font-size:34px}
.hero h1{position:absolute;top:265px;width:1200px;text-align:center;font-weight:300;font-size:35px;color:#fff}
.hero p{position:absolute;top:330px;left:240px;width:720px;text-align:center;font-family:"Open Sans",sans-serif;font-size:16px;line-height:1.8;color:#e5e8ec}
.hero .arrow{position:absolute;top:345px}
.hero .dots{position:absolute;top:455px;width:1200px;display:flex;justify-content:center;gap:10px}
.hero .dots span{width:9px;height:9px;border-radius:50%;background:var(--orange)}
.hero .dots span.off{background:#9aa1aa}
.hero .scroll-hint{position:absolute;top:510px;left:588px}

/* nav */
.site-nav{top:788px;height:134px;background:var(--paper);border-bottom:1px solid var(--line)}
.site-nav .brand-mark{top:46px;left:110px;font-size:30px}
.site-nav ul{list-style:none;position:absolute;top:0;right:108px;height:100px;display:flex}
.site-nav li{font-size:13px;font-weight:700;letter-spacing:1px;color:var(--ink);padding:0 22px;display:flex;align-items:center;height:100px}
.site-nav li.active{background:var(--orange);color:#fff;padding:0 30px;margin-top:0}

/* who */
.who{top:922px;height:620px}
.who .section-title{margin-top:68px}
.who .section-lead{width:680px;margin-top:14px}
.personas{position:absolute;top:183px;left:110px;width:980px;display:flex;justify-content:space-between}
.persona{width:225px;text-align:center;position:relative}
.persona svg{display:block;margin:0 auto}
.persona h3{font-size:12px;font-weight:700;letter-spacing:.5px;margin-top:18px;color:var(--ink)}
.persona p{font-family:"Open Sans",sans-serif;font-size:12px;line-height:1.7;color:var(--muted);margin:8px 16px 0}
.persona.featured::before{content:"";position:absolute;left:0;top:85px;width:225px;height:250px;background:var(--amber);z-index:-1}
.persona.featured h3,.persona.featured p{color:#fff}
.who .personas{z-index:1}

/* about */
.about{top:1542px;height:469px;background:linear-gradient(180deg,#1c2330,#202a38 60%,#161c26)}
.about::before{content:"";position:absolute;inset:0;background:linear-gradient(100deg,rgba(80,92,110,.35),rgba(20,26,34,.1) 45%,rgba(90,100,118,.3) 80%)}
.about .section-title{position:relative;color:#fff;margin-top:95px}
.about .subtitle{position:relative;font-family:"Open Sans",sans-serif;font-size:14px;color:#d5d9de;text-align:center;margin-top:8px}
.about .statement{position:absolute;top:196px;left:110px;width:470px;font-size:25px;line-height:1.4;font-weight:400;color:#fff}
.about .detail{position:absolute;top:196px;left:613px;width:480px;font-family:"Open Sans",sans-serif;font-size:12.5px;line-height:1.75;color:#c9ced5}
.about .detail p+p{margin-top:14px}

/* services */
.services{top:2011px;height:570px}
.services .section-title{margin-top:100px}
.services .section-lead{width:700px;margin-top:12px}
.service-list{position:absolute;top:241px;left:110px;width:980px;display:flex;gap:40px}
.service{flex:1;display:flex;gap:14px;padding:20px 16px;min-height:162px}
.service.featured{background:var(--amber)}
.service h3{font-size:11.5px;font-weight:700;letter-spacing:.3px;line-height:1.5;color:var(--ink)}
.service p{font-family:"Open Sans",sans-serif;font-size:12px;line-height:1.65;color:var(--muted);margin-top:8px}
.service.featured h3,.service.featured p{color:#fff}
.service svg{flex:none}
.more-btn{position:absolute;top:442px;left:553px;width:94px;height:44px;background:var(--orange);color:#fff;font-size:12px;font-weight:700;letter-spacing:1px;display:flex;align-items:center;justify-content:center}

/* partners */
.partners{top:2581px;height:419px;background:var(--mist)}
.partners .section-title{margin-top:105px}
.partners .section-lead{width:720px;margin-top:12px}
.partner-row{position:absolute;top:248px;left:130px;width:940px;display:flex;justify-content:space-between}

/* footer */
.site-footer{top:3000px;height:352px;background:var(--paper);border-top:1px solid var(--line)}
.footer-col{position:absolute;top:40px}
.footer-col h4{font-size:11px;font-weight:700;letter-spacing:1px;color:var(--ink);margin-bottom:18px}
.footer-col ul{list-style:none}
.footer-col li{font-family:"Open Sans",sans-serif;font-size:12px;color:var(--muted);line-height:2;display:flex;align-items:center;gap:8px}
.footer-col li::before{content:"";width:5px;height:5px;background:var(--orange)}
.contact-line{display:flex;gap:10px;align-items:flex-start;font-family:"Open Sans",sans-serif;font-size:12px;color:var(--muted);line-height:1.6;margin-bottom:14px}
.contact-line a{color:var(--orange);text-decoration:none}
.social{display:flex;gap:8px}
.social span{width:22px;height:22px;background:var(--orange)}
.footer-brand{position:absolute;right:60px;top:140px;font-size:88px;font-weight:700;color:var(--orange);letter-spacing:-1px;display:flex;align-items:center;gap:16px}
.footer-brand .dot{width:30px;height:30px;background:var(--orange)}
</style>
</head>
<body>

<header class="hero">
  <div class="hero-backdrop" role="img" aria-label="Photograph looking up at glass office towers against a dark sky"></div>
  <div class="brand-mark"><span class="dot"></span>Veltra</div>
  <h1>You need integration. We're always there with you.</h1>
  <p>Veltra is one of the leading systems integrators to the world's finance sector. We are an extension of your business and our services portfolio has been built so you always have access to a complete partner.</p>
  <svg class="arrow" style="left:110px" width="16" height="26" viewBox="0 0 16 26"><path d="M13 2 3 13l10 11" fill="none" stroke="#fff" stroke-width="3"/></svg>
  <svg class="arrow" style="left:1074px" width="16" height="26" viewBox="0 0 16 26"><path d="M3 2l10 11L3 24" fill="none" stroke="#fff" stroke-width="3"/></svg>
  <div class="dots"><span></span><span></span><span class="off"></span></div>
  <svg class="scroll-hint" width="24" height="38" viewBox="0 0 24 38"><rect x="2" y="2" width="20" height="34" rx="10" fill="none" stroke="#fff" stroke-width="2"/><rect x="11" y="9" width="2" height="7" fill="#fff"/></svg>
</header>

<nav class="site-nav">
  <div class="brand-mark"><span class="dot"></span>Veltra</div>
  <ul>
    <li class="active">ABOUT</li>
    <li>SERVICES</li>
    <li>PARTNERS</li>
    <li>CLIENTS</li>
    <li>CONTACT</li>
  </ul>
</nav>

<section class="who">
  <h2 class="section-title">Who Are You</h2>
  <p class="section-lead">If you're part of a financial organisation, we have the power to help everyone work more efficiently, productively and profitably.</p>
  <div class="personas">
    <article class="persona featured">
      <svg width="150" height="170" viewBox="0 0 150 170" role="img" aria-label="Portrait photo of a senior fund manager"><defs><linearGradient id="p1" x1="0" y1="0" x2="0" y2="1"><stop offset="0" stop-color="#d9dde2"/><stop offset="1" stop-color="#7c8592"/></linearGradient></defs><polygon points="75,5 145,45 145,125 75,165 5,125 5,45" fill="url(#p1)" stroke="#fff" stroke-width="4"/></svg>
      <h3>SENIOR/HEAD FUND MANAGER</h3>
      <p>You need to develop and implement strategies for business growth and profit. Your biggest asset is your staff, and a happy workforce is a productive one.</p>
    </article>
    <article class="persona">
      <svg width="150" height="170" viewBox="0 0 150 170" role="img" aria-label="Portrait photo of a chief technology officer"><defs><linearGradient id="p2" x1="0" y1="0" x2="0" y2="1"><stop offset="0" stop-color="#e4e6e9"/><stop offset="1" stop-color="#4d5560"/></linearGradient></defs><polygon points="75,5 145,45 145,125 75,165 5,125 5,45" fill="url(#p2)"/></svg>
      <h3>CTO</h3>
      <p>Your key responsibility is to obtain the maximum ROI from products and services. You understand investment opportunities, providing they return higher efficiencies and revenues.</p>
    </article>
    <article class="persona">
      <svg width="150" height="170" viewBox="0 0 150 170" role="img" aria-label="Portrait photo of an IT manager"><defs><linearGradient id="p3" x1="0" y1="0" x2="0" y2="1"><stop offset="0" stop-color="#eceef0"/><stop offset="1" stop-color="#8a8f96"/></linearGradient></defs><polygon points="75,5 145,45 145,125 75,165 5,125 5,45" fill="url(#p3)"/></svg>
      <h3>IT MANAGER / CTO</h3>
      <p>Integration with partners and services is your key concern. You want to make sure any IT system you implement will work with the whole infrastructure of your company.</p>
    </article>
    <article class="persona">
      <svg width="150" height="170" viewBox="0 0 150 170" role="img" aria-label="Portrait photo of an employee"><defs><linearGradient id="p4" x1="0" y1="0" x2="0" y2="1"><stop offset="0" stop-color="#f1f2f3"/><stop offset="1" stop-color="#a9b2bc"/></linearGradient></defs><polygon points="75,5 145,45 145,125 75,165 5,125 5,45" fill="url(#p4)"/></svg>
      <h3>EMPLOYEES</h3>
      <p>You're working hard but not getting anywhere fast. You want the tools to make your job easier so you can spend more time thinking about what you're doing rather than how you're doing it.</p>
    </article>
  </div>
</section>

<section class="about" role="img" aria-label="Dark photograph of city skyscrapers behind the About section">
  <h2 class="section-title">About Veltra</h2>
  <p class="subtitle">If we know something won't benefit your business, we won't do it.</p>
  <p class="statement">Veltra is one of the leading systems integrators to the world's financial sector. We have more than 40 years' experience working with high profile financial organisations. We always strive for mutual growth.</p>
  <div class="detail">
    <p>Consider us as an extension of your business. We work with everyone in your organisation to develop strategies and implement market-leading solutions to strengthen your footprint against your competition.</p>
    <p>Our holistic and progressive approach to serving clients ensures we build trusted, long-term relationships. We identify key areas to help clients achieve their most important business objectives efficiently to maximise return on investment.</p>
  </div>
</section>

<section class="services">
  <h2 class="section-title">Our Services</h2>
  <p class="section-lead">We are a world-class systems integrator with a wide range of expertise within the technology market, with no sector left unexplored.</p>
  <div class="service-list">
    <article class="service featured">
      <svg width="40" height="44" viewBox="0 0 40 44"><polygon points="20,1 39,12 39,32 20,43 1,32 1,12" fill="none" stroke="#fff" stroke-width="2"/><rect x="12" y="14" width="16" height="5" fill="#fff"/><rect x="12" y="21" width="16" height="5" fill="#fff"/><rect x="12" y="28" width="16" height="3" fill="#fff"/></svg>
      <div><h3>DATA CENTRE &amp; INFRASTRUCTURE</h3><p>Veltra offers analysis, assessment, implementation and management of your infrastructure to boost your company's connectivity and profitability.</p></div>
    </article>
    <article class="service">
      <svg width="40" height="44" viewBox="0 0 40 44"><polygon points="20,1 39,12 39,32 20,43 1,32 1,12" fill="none" stroke="#f29111" stroke-width="2"/><path d="M13 22l5 5 9-10" fill="none" stroke="#f29111" stroke-width="2.5"/></svg>
      <div><h3>IT SUPPORT, MANAGED AND PROFESSIONAL SERVICES</h3><p>Veltra built its reputation on IT support, managed and professional services and it continues to operate with these as a priority.</p></div>
    </article>
    <article class="service">
      <svg width="40" height="44" viewBox="0 0 40 44"><polygon points="20,1 39,12 39,32 20,43 1,32 1,12" fill="none" stroke="#f29111" stroke-width="2"/><circle cx="20" cy="22" r="3" fill="#f29111"/><circle cx="12" cy="16" r="2.5" fill="#f29111"/><circle cx="28" cy="16" r="2.5" fill="#f29111"/><circle cx="20" cy="31" r="2.5" fill="#f29111"/><path d="M12 16l8 6 8-6M20 22v9" stroke="#f29111" stroke-width="1.5" fill="none"/></svg>
      <div><h3>VOICE &amp; DATA NETWORKS</h3><p>Veltra can offer hosted Voice over IP (VoIP) and hosted traditional PBX systems based around a flexible, mobile and agile platform.</p></div>
    </article>
  </div>
  <div class="more-btn">MORE</div>
</section>

<section class="partners">
  <h2 class="section-title">Partners</h2>
  <p class="section-lead">We have carefully selected our partners to help your business grow how you want it to. All our partners have the same values as we do, making sure their solutions seamlessly integrate with your organisation.</p>
  <div class="partner-row">
    <svg width="96" height="108" viewBox="0 0 96 108" role="img" aria-label="Partner badge"><polygon points="48,2 94,28 94,80 48,106 2,80 2,28" fill="#fff" stroke="#dadde1" stroke-width="2"/></svg>
    <svg width="96" height="108" viewBox="0 0 96 108" role="img" aria-label="Partner badge"><polygon points="48,2 94,28 94,80 48,106 2,80 2,28" fill="#fff" stroke="#dadde1" stroke-width="2"/></svg>
    <svg width="96" height="108" viewBox="0 0 96 108" role="img" aria-label="Partner badge"><polygon points="48,2 94,28 94,80 48,106 2,80 2,28" fill="#fff" stroke="#dadde1" stroke-width="2"/></svg>
    <svg width="96" height="108" viewBox="0 0 96 108" role="img" aria-label="Partner badge"><polygon points="48,2 94,28 94,80 48,106 2,80 2,28" fill="#fff" stroke="#dadde1" stroke-width="2"/></svg>
    <svg width="96" height="108" viewBox="0 0 96 108" role="img" aria-label="Partner badge"><polygon points="48,2 94,28 94,80 48,106 2,80 2,28" fill="#fff" stroke="#dadde1" stroke-width="2"/></svg>
    <svg width="96" height="108" viewBox="0 0 96 108" role="img" aria-label="Partner badge"><polygon points="48,2 94,28 94,80 48,106 2,80 2,28" fill="#fff" stroke="#dadde1" stroke-width="2"/></svg>
  </div>
</section>

<footer class="site-footer">
  <div class="footer-col" style="left:110px">
    <h4>NAVIGATION</h4>
    <ul><li>Home</li><li>About</li><li>Services</li><li>Partners</li><li>Clients</li><li>Contact</li></ul>
  </div>
  <div class="footer-col" style="left:278px;width:170px">
    <h4>CONTACT US</h4>
    <div class="contact-line"><svg width="12" height="16" viewBox="0 0 12 16"><path d="M6 1a5 5 0 0 1 5 5c0 4-5 9-5 9S1 10 1 6a5 5 0 0 1 5-5z" fill="#f29111"/><circle cx="6" cy="6" r="2" fill="#fff"/></svg><span>12 Example Row,<br>London<br>EC3M 7XX</span></div>
    <div class="contact-line"><svg width="12" height="14" viewBox="0 0 12 14"><path d="M2 1h3l1 3-2 1.5a8 8 0 0 0 3.5 3.5L9 7l3 1v3c0 1-1 2-2 2A10 10 0 0 1 0 3c0-1 1-2 2-2z" fill="#f29111"/></svg><span>+44 (0)20 7946 0000</span></div>
    <div class="contact-line"><svg width="14" height="10" viewBox="0 0 14 10"><rect width="14" height="10" fill="#f29111"/><path d="M0 0l7 6 7-6" fill="none" stroke="#fff" stroke-width="1.2"/></svg><a>hello@veltra-example.co.uk</a></div>
  </div>
  <div class="footer-col" style="left:446px">
    <h4>CONNECT</h4>
    <div class="social"><span role="img" aria-label="Social profile link"></span><span role="img" aria-label="Social profile link"></span></div>
  </div>
  <div class="footer-brand"><span class="dot"></span>Veltra</div>
</footer>

</body>
</html>
```